Flyer Design

we need a flyer designing for our independent estate and letting agents based in Gosport Hampshire, our company name is Farrow and Partners Gosport, our contact details are 37 Willowmere Lane, Gosport, Hampshire PO13 4TJ, 02392 784630, email :tamsin@farrowpartners-example.co.uk. Our special offer we'd like to advertise is for the year 2015 we aim to sell 100 properties and only charge £1000 no vat sellers fee for each property sold. We are also offering a free no obligation market appraisal by one of our professional assessors. The flyer must have this disclaimer added to the bottom of it: if you are currently on the market with another agent then your current terms and conditions may need to be reviewed prior to changing agency. We advertise on Homevista and would like to see designs that use the colours lime green and navy blue. The final design should be eye catching and promote this special offer.

```html
<!DOCTYPE html>
<html lang="en">
<head>
<meta charset="utf-8">
<title>Farrow and Partners – 2015 Seller Offer</title>
<link rel="stylesheet" href="https://fonts.googleapis.com/css2?family=Roboto:wght@400;500;700;900&family=Tinos:wght@400&display=swap">
<style>
:root{
  --surround:#4a2d02;
  --navy:#050c26;
  --lime:#5dfc0a;
  --white:#ffffff;
  --ink:#111111;
  --label-bg:rgba(20,20,20,0.82);
  --footer:#1f2223;
  --muted:#c9cccd;
}
*{margin:0;padding:0;box-sizing:border-box}
html,body{width:1200px;height:1000px;overflow:hidden;background:var(--surround)}
.canvas{position:relative;width:1200px;height:1000px;background:var(--surround)}
.flyer{position:absolute;left:251px;top:0;width:699px;height:1000px;background:var(--white);font-family:'Roboto',Arial,sans-serif}
.masthead{height:108px;background:var(--navy);display:flex;flex-direction:column;align-items:center;justify-content:center;color:var(--white)}
.brand-name{font-family:'Tinos','Times New Roman',serif;font-size:24px;line-height:1;letter-spacing:.5px}
.brand-tag{font-family:'Tinos','Times New Roman',serif;font-size:7px;letter-spacing:2px;margin-top:8px;text-align:center;line-height:1.3}
.hero{position:relative;height:281px;overflow:hidden}
.hero-photo{position:absolute;inset:0;background:linear-gradient(180deg,#b8ad93 0%,#8d7d62 45%,#5c4a36 75%,#6b5238 100%)}
.hero-copy{position:relative;text-align:center;color:var(--white);text-shadow:0 2px 6px rgba(0,0,0,.55)}
.hero-head{font-weight:700;font-size:39px;line-height:48px;padding-top:42px}
.hero-year{font-weight:900;font-size:92px;line-height:82px;color:#f1f1f1;margin-top:6px}
.hero-note{font-weight:500;font-size:18px;line-height:22px;margin-top:0}
.offer-band{height:98px;background:var(--lime);color:var(--white);display:flex;align-items:center;justify-content:center;text-align:center;font-weight:700;font-size:23px;line-height:32px;padding:0 24px}
.featured{height:428px;position:relative}
.featured-title{font-family:'Tinos','Times New Roman',serif;font-weight:400;font-size:23px;color:var(--ink);text-align:center;padding-top:12px}
.home-card{position:absolute;width:205px;height:167px}
.home-photo{position:absolute;inset:0}
.home-label{position:absolute;left:8px;right:8px;bottom:0;height:43px;background:var(--label-bg);color:var(--white);text-align:center;padding-top:5px;font-family:Arial,'Roboto',sans-serif}
.home-name{font-weight:700;font-size:14px;line-height:17px;letter-spacing:.3px}
.home-address{font-size:11px;line-height:15px}
.contact-bar{position:absolute;left:0;top:915px;width:699px;height:85px;background:var(--footer);color:var(--white);font-family:Arial,'Roboto',sans-serif}
.contact-left{position:absolute;left:15px;top:18px}
.contact-right{position:absolute;left:430px;top:6px}
.contact-heading{font-weight:700;font-size:14px;margin-bottom:6px}
.contact-right .contact-heading{font-size:15px;margin-bottom:3px}
.contact-line{font-size:14px;line-height:19px}
.disclaimer{position:absolute;left:15px;right:15px;top:71px;font-size:9px;line-height:11px;color:var(--muted);white-space:nowrap;text-align:center}
</style>
</head>
<body>
<div class="canvas">
  <main class="flyer">
    <header class="masthead">
      <div class="brand-name">Farrow and Partners</div>
      <div class="brand-tag">ESTATE &amp; LETTING<br>AGENTS</div>
    </header>

    <section class="hero">
      <div class="hero-photo" role="img" aria-label="Photo of a bright bedroom with an iron bed, armchair and rug"></div>
      <div class="hero-copy">
        <p class="hero-head">We are selling 100 properties and<br>only charging £1000 for each in</p>
        <p class="hero-year">2015</p>
        <p class="hero-note">No VAT sellers fee for each property sold</p>
      </div>
    </section>

    <section class="offer-band">
      <p>We are also offering a free no obligation market appraisal by one of our professional assessors</p>
    </section>

    <section class="featured">
      <h2 class="featured-title">Some of Our Featured Homes</h2>

      <article class="home-card" style="left:15px;top:59px">
        <div class="home-photo" role="img" aria-label="Photo of a stone cottage in green hills" style="background:linear-gradient(180deg,#dfe9f0 0%,#a7c98a 40%,#6fae3c 100%)"></div>
        <div class="home-label"><div class="home-name">Churchill House</div><div class="home-address">4586 Saint Rd, London</div></div>
      </article>
      <article class="home-card" style="left:248px;top:59px">
        <div class="home-photo" role="img" aria-label="Photo of a white villa with blue shutters and flowers" style="background:linear-gradient(180deg,#8fc3ea 0%,#f2f2f0 35%,#e9e6e0 70%,#6c8a3c 100%)"></div>
        <div class="home-label"><div class="home-name">Sir Creek’s House</div><div class="home-address">5316 Creek Rd, London</div></div>
      </article>
      <article class="home-card" style="left:481px;top:59px">
        <div class="home-photo" role="img" aria-label="Photo of a Georgian brick terrace street" style="background:linear-gradient(180deg,#cfe0ee 0%,#8a7a62 30%,#5f5344 100%)"></div>
        <div class="home-label"><div class="home-name">Richmond House</div><div class="home-address">4786 Richmond Rd, London</div></div>
      </article>

      <article class="home-card" style="left:15px;top:239px">
        <div class="home-photo" role="img" aria-label="Photo of an ornate red brick mansion block" style="background:linear-gradient(180deg,#d6dde4 0%,#a0624a 40%,#7b4634 100%)"></div>
        <div class="home-label"><div class="home-name">Tropico Mansion</div><div class="home-address">2156 Brick Rd, London</div></div>
      </article>
      <article class="home-card" style="left:248px;top:239px">
        <div class="home-photo" role="img" aria-label="Photo of a peach painted townhouse" style="background:linear-gradient(180deg,#9ec8e6 0%,#e3b991 40%,#c99a70 100%)"></div>
        <div class="home-label"><div class="home-name">Raymond House</div><div class="home-address">3296 Alberta Rd, London</div></div>
      </article>
      <article class="home-card" style="left:481px;top:239px">
        <div class="home-photo" role="img" aria-label="Photo of colourful historic townhouses on a square" style="background:linear-gradient(180deg,#4e8fd0 0%,#9fc2e3 30%,#d9a85a 60%,#8a6a4a 100%)"></div>
        <div class="home-label"><div class="home-name">Dalhousie House</div><div class="home-address">121 Dalhousie Sq. London</div></div>
      </article>
    </section>

    <footer class="contact-bar">
      <div class="contact-left">
        <p class="contact-heading">Contact</p>
        <p class="contact-line">Email: tamsin@farrowpartners-example.co.uk</p>
      </div>
      <div class="contact-right">
        <p class="contact-heading">LOCATION</p>
        <p class="contact-line">37 Willowmere Lane, Gosport,<br>Hampshire PO13 4TJ, 02392 784630</p>
      </div>
      <p class="disclaimer">If you are currently on the market with another agent then your current terms and conditions may need to be reviewed prior to changing agency.</p>
    </footer>
  </main>
</div>
</body>
</html>
```